Invite Card (Ministers) (business cards used for personal invitation to our church)

I need a business card sized advertisement. The card is a replacement for the attached card only much much cooler. I do not want a image background but more of a vectored, flat look with advertising colors.

I have attached a new image of the couple to replace the old image and a new logo to replace the old logo.

I need a PSD with ALL of the layers un-merged & unlocked

The back of the card should carry the same information as the old card.

Use advertising color and a modern flat look and feel.

Target Market(s)

professional audience

Industry/Entity Type

Non-Profit

Contact Information for Business Card

The card is a replacement for the attached card only much much cooler. I do not want a image background but more of a vectored, flat look with advertising colors.

Font styles to use
Sans Serif

Requirements
Must have
• Must have new logo, new image of couple
Should not have
• graphical background

```html
<!DOCTYPE html>
<html lang="en">
<head>
<meta charset="utf-8">
<title>Grace Revealed – Invitation Card</title>
<link href="https://fonts.googleapis.com/css2?family=Open+Sans:wght@400;600;700;800&family=Caveat:wght@500&display=swap" rel="stylesheet">
<style>
  :root {
    --stage: #2a2a2c;
    --blue-deep: #1a78c6;
    --blue-mid: #2a8fd6;
    --blue-light: #3ea6dc;
    --indigo: #2c2f9c;
    --indigo-soft: #4145b2;
    --white: #ffffff;
    --photo-a: #6b6f86;
    --photo-b: #b49ac8;
  }
  * { box-sizing: border-box; margin: 0; padding: 0; }
  html, body { width: 1200px; height: 900px; overflow: hidden; }
  body {
    background: var(--stage);
    font-family: "Open Sans", Arial, sans-serif;
    position: relative;
  }
  .card {
    position: absolute;
    left: 250px;
    width: 700px;
    height: 400px;
    overflow: hidden;
    background: linear-gradient(100deg, var(--blue-deep) 0%, var(--blue-mid) 55%, var(--blue-light) 100%);
    color: var(--white);
  }
  .card--back { top: 35px; }
  .card--front { top: 465px; }

  /* back side */
  .contact {
    position: absolute;
    left: 48px;
    top: 78px;
    font-style: normal;
    font-size: 15px;
    line-height: 1.3;
    letter-spacing: 0.5px;
    color: rgba(255,255,255,0.88);
  }
  .contact .phone { font-weight: 700; color: var(--white); }
  .schedule {
    position: absolute;
    left: 60px;
    top: 250px;
    width: 330px;
    list-style: none;
    font-size: 14px;
    letter-spacing: 1px;
    z-index: 1;
  }
  .schedule li {
    display: flex;
    align-items: baseline;
    margin-bottom: 12px;
    white-space: nowrap;
  }
  .schedule .leader {
    flex: 1;
    border-bottom: 2px dotted rgba(255,255,255,0.85);
    margin: 0 4px;
    transform: translateY(-4px);
  }
  .brand-small {
    position: absolute;
    right: 36px;
    top: 30px;
    display: flex;
    align-items: center;
    gap: 8px;
    font-size: 15px;
    font-weight: 700;
    color: var(--indigo);
  }
  .brand-small .mark {
    width: 22px; height: 22px;
    background: var(--white);
    border-radius: 3px;
  }
  .couple-photo {
    position: absolute;
    right: 12px;
    bottom: 0;
    width: 270px;
    height: 230px;
    background: linear-gradient(90deg, var(--photo-a), var(--photo-b));
    border-radius: 110px 110px 0 0;
  }

  /* front side */
  .invite {
    position: absolute;
    left: 58px;
    top: 48px;
    font-family: "Caveat", cursive;
    font-size: 42px;
    line-height: 0.95;
    transform: rotate(-6deg);
    transform-origin: left top;
  }
  .invite span { display: block; padding-left: 18px; }
  .brand {
    position: absolute;
    left: 240px;
    top: 120px;
    display: flex;
    align-items: center;
    gap: 14px;
    font-size: 38px;
    font-weight: 800;
    letter-spacing: 0.5px;
    white-space: nowrap;
    color: var(--white);
  }
  .brand .mark {
    width: 42px; height: 42px;
    background: var(--indigo);
    border-radius: 6px;
  }
  .waves {
    position: absolute;
    left: 0; bottom: 0;
    width: 700px; height: 230px;
  }
</style>
</head>
<body>

<section class="card card--back" aria-label="Card back">
  <div class="brand-small"><span class="mark"></span>Grace Revealed</div>
  <address class="contact">
    gracerevealed.org<br>
    48 Oak Hollow Lane &nbsp;· Brookdale ,Tx 75000<br>
    <span class="phone">1-800-555-0142</span>
  </address>
  <ul class="schedule">
    <li>SUNDAY<span class="leader"></span>9:00AM</li>
    <li>SUNDAY<span class="leader"></span>11:00AM</li>
    <li>WED.Bible Class<span class="leader"></span>7:00PM</li>
  </ul>
  <div class="couple-photo" role="img" aria-label="Photo of the ministers, a smiling couple"></div>
</section>

<section class="card card--front" aria-label="Card front">
  <p class="invite">You’re<span>Invited</span></p>
  <div class="brand"><span class="mark"></span>Grace Revealed</div>
  <svg class="waves" viewBox="0 0 700 230" preserveAspectRatio="none" aria-hidden="true">
    <path d="M0 170 C 180 150, 330 190, 470 110 C 560 60, 640 40, 700 30 L700 230 L0 230 Z" fill="var(--indigo-soft)"/>
    <path d="M150 215 C 320 200, 440 150, 540 95 C 600 60, 650 40, 700 28 L700 45 C 640 58, 590 80, 540 110 C 440 170, 320 210, 150 215 Z" fill="var(--white)"/>
    <path d="M0 195 C 200 190, 380 200, 520 140 C 600 105, 660 80, 700 70 L700 230 L0 230 Z" fill="var(--indigo)"/>
  </svg>
</section>

</body>
</html>
```